Flyer to be utilised on social media and email marketing - Making Divorce Applications Affordable

Finalising Your Divorce Made Easy <br/><br/>Are you separated and both seeking to Divorce? At Brellis & Brellis Legal we provide a cost effective way for this to occur.... <br/><br/>OLD APPROACH <br/> Arrange a meeting with a solicitor <br/> Attend appointment <br/> Provide background information to the lawyer <br/> Lawyer to draft document <br/> Lawyer to contact you to obtain further instructions, if required <br/>Lawyer to amend divorce application, if further amendments required <br/> Lawyer to send you a copy of the draft Divorce Application<br/>Lawyer to make further changes, if required <br/>Lawyer to resend you draft Divorce Application, if required <br/>Lawyer to organise an appointment to attend office to sign Divorce Application <br/>TIME CONSUMING & COSTLY - CAN COST OVER $3500 <br/><br/>NEW APPROACH <br/> We send you a Form <br/> You complete the Form <br/> We review your instructions <br/>We provide you with advicee <br/>We draft Divorce Application and send to you for review <br/> QUICK & SIMPLE PROCESS - FIXED COST OF $799 INCLUSIVE OF GST <br/><br/>Please include the OLD APPROACH ON THE LEFT SIDE AND NEW APPROACH ON THE RIGHT SIDE OF THE PAGE (SO THAT THEY ARE NEXT TO EACH OTHER)<br/><br/>*Terms and Conditions - Applies to simple joint divorce applications, no court appearances, no drafting or finalising any further court documentations, and excludes disbursements costs including court filing fee <br/>

Target Market(s)

Separated Families - Individuals from 35+

Industry/Entity Type

Legal

Font styles to use
Serif

Colors
0255a3

Requirements
Must have
• Please include website - www.brellisandbrellislegal.com.au
• Email - office@brellisandbrellislegal.com.au
• Logo Colour - Royal blue colour #10416a or hex code #063169

```html
<!DOCTYPE html>
<html lang="en">
<head>
<meta charset="utf-8">
<title>Finalising Your Divorce Made Easy – Brellis &amp; Brellis Legal</title>
<link rel="stylesheet" href="https://fonts.googleapis.com/css2?family=Cinzel:wght@500;600&family=Lato:wght@400;700&display=swap">
<style>
  :root {
    --navy: #0f416b;
    --ink: #1a1f2b;
    --brand: #134a7c;
    --orange: #f39a2b;
    --white: #ffffff;
    --sky-light: #dcebf6;
    --sky-mid: #3a78a8;
    --stage: #ebe7e1;
  }
  * { margin: 0; padding: 0; box-sizing: border-box; }
  html, body { width: 1200px; height: 1134px; overflow: hidden; background: var(--stage); }
  .flyer {
    position: absolute; left: 214px; top: 20px; width: 771px; height: 1094px;
    overflow: hidden;
    background: linear-gradient(180deg, var(--sky-light) 0%, #8db9da 9%, var(--sky-mid) 22%, #1d5586 36%, var(--navy) 48%, var(--navy) 100%);
    font-family: "Lato", sans-serif;
  }
  .sky-art { position: absolute; right: 0; top: 0; width: 260px; height: 420px; }
  .curtain { position: absolute; left: 0; top: 0; width: 771px; height: 1094px; }
  .block { position: absolute; }
  .title {
    left: 49px; top: 46px;
    font-family: "Cinzel", serif; font-weight: 600; color: var(--brand);
    font-size: 66px; line-height: 62px; letter-spacing: 0.5px; white-space: nowrap;
  }
  .intro { left: 49px; top: 187px; width: 420px; color: var(--ink); font-size: 17.5px; line-height: 22px; }
  .heading {
    font-family: "Cinzel", serif; font-weight: 500; font-size: 27px; line-height: 30px; text-transform: uppercase;
  }
  .old { left: 49px; top: 282px; width: 318px; color: var(--ink); }
  .old .heading { color: var(--brand); margin-bottom: 3px; }
  .steps { list-style: none; font-size: 17.3px; line-height: 22px; }
  .steps li { position: relative; padding-left: 15px; }
  .steps li::before { content: "•"; position: absolute; left: 0; top: 0; }
  .old .steps li::before { color: var(--brand); }
  .new .steps li::before { color: var(--orange); }
  .tag { font-weight: 700; font-size: 18px; line-height: 22px; text-transform: uppercase; letter-spacing: -0.2px; }
  .price { font-weight: 700; font-size: 25.5px; line-height: 31px; text-transform: uppercase; }
  .price sup { font-size: 13px; vertical-align: 10px; }
  .old-cost { left: 49px; top: 736px; color: var(--brand); }
  .old-cost .price { margin-top: 5px; }
  .new { left: 477px; top: 512px; width: 262px; color: var(--white); }
  .new .heading { color: var(--orange); margin-bottom: 3px; }
  .new-cost { left: 477px; top: 701px; color: var(--orange); }
  .new-cost .price { margin-top: 7px; }
  .brand-name {
    left: 41px; top: 930px; width: 330px; text-align: center; white-space: nowrap;
    font-family: "Cinzel", serif; font-weight: 600; color: var(--brand); font-size: 23px; line-height: 30px;
  }
  .contact { left: 41px; top: 1017px; color: var(--ink); font-size: 17.3px; line-height: 22px; font-style: normal; }
  .contact p { display: flex; align-items: center; gap: 5px; }
  .contact svg { width: 15px; height: 15px; flex: none; }
  .terms { left: 477px; top: 899px; width: 250px; color: var(--white); }
  .terms h2 { font-size: 17px; font-weight: 700; line-height: 22px; margin-bottom: 3px; }
  .terms p { font-size: 13px; line-height: 17.7px; }
</style>
</head>
<body>
  <main class="flyer">
    <svg class="sky-art" viewBox="0 0 260 420" role="img" aria-label="Photograph of a bright sky with scattered clouds over deep blue">
      <defs>
        <radialGradient id="glow" cx="0.85" cy="0.05" r="0.8">
          <stop offset="0" stop-color="#ffffff" stop-opacity="0.85"/>
          <stop offset="1" stop-color="#ffffff" stop-opacity="0"/>
        </radialGradient>
      </defs>
      <rect width="260" height="420" fill="url(#glow)"/>
    </svg>

    <svg class="curtain" viewBox="0 0 771 1094" role="img" aria-label="Photograph of a white drawn stage curtain tied back with a navy rope">
      <defs>
        <linearGradient id="folds" x1="0" x2="1" y1="0" y2="0">
          <stop offset="0" stop-color="#d9d9d9"/>
          <stop offset="0.12" stop-color="#eeeeee"/>
          <stop offset="0.25" stop-color="#d4d4d4"/>
          <stop offset="0.4" stop-color="#f3f3f3"/>
          <stop offset="0.55" stop-color="#dadada"/>
          <stop offset="0.72" stop-color="#f6f6f6"/>
          <stop offset="0.88" stop-color="#e2e2e2"/>
          <stop offset="1" stop-color="#fbfbfb"/>
        </linearGradient>
      </defs>
      <path d="M0,0 L551,0 C540,100 530,150 524,202 C505,350 490,450 471,508 C440,620 400,720 395,819 C392,920 410,1010 422,1094 L0,1094 Z" fill="url(#folds)"/>
    </svg>

    <h1 class="block title">Finalising Your<br>Divorce Made Easy</h1>

    <p class="block intro">Are you separated and both seeking to Divorce? At Brellis &amp; Brellis Legal we provide a cost effective way for this to occur</p>

    <section class="block old">
      <h2 class="heading">Old Approach</h2>
      <ul class="steps">
        <li>Arrange a meeting with a solicitor</li>
        <li>Attend appointment</li>
        <li>Provide background information to the lawyer</li>
        <li>Lawyer to draft document</li>
        <li>Lawyer to contact you to obtain further instructions, if required</li>
        <li>Lawyer to amend divorce application, if further amendments required</li>
        <li>Lawyer to send you a copy of the draft Divorce Application</li>
        <li>Lawyer to make further changes, if required</li>
        <li>Lawyer to resend you draft Divorce Application, if required</li>
        <li>Lawyer to organise an appointment to attend office to sign Divorce Application</li>
      </ul>
    </section>

    <div class="block old-cost">
      <p class="tag">Time consuming &amp; costly</p>
      <p class="price">Can cost over <sup>$</sup>3500</p>
    </div>

    <section class="block new">
      <h2 class="heading">New Approach</h2>
      <ul class="steps">
        <li>We send you a Form</li>
        <li>You complete the Form</li>
        <li>We review your instructions</li>
        <li>We provide you with advicee</li>
        <li>We draft Divorce Application and send to you for review</li>
      </ul>
    </section>

    <div class="block new-cost">
      <p class="tag">Quick &amp; simple process</p>
      <p class="price">Fixed cost of <sup>$</sup>799<br>inclusive of GST</p>
    </div>

    <p class="block brand-name">Brellis &amp; Brellis Legal</p>

    <address class="block contact">
      <p>
        <svg viewBox="0 0 16 16" aria-hidden="true"><rect x="1" y="3" width="14" height="10" rx="1.5" fill="none" stroke="#134a7c" stroke-width="1.6"/><path d="M1.5 4 8 9l6.5-5" fill="none" stroke="#134a7c" stroke-width="1.6"/></svg>
        office@brellisandbrellislegal.com.au
      </p>
      <p>
        <svg viewBox="0 0 16 16" aria-hidden="true"><g fill="none" stroke="#134a7c" stroke-width="1.3"><circle cx="8" cy="8" r="6.8"/><ellipse cx="8" cy="8" rx="3" ry="6.8"/><path d="M1.2 8h13.6M2.3 4.5h11.4M2.3 11.5h11.4"/></g></svg>
        www.brellisandbrellislegal.com.au
      </p>
    </address>

    <section class="block terms">
      <h2>*Terms and Conditions</h2>
      <p>Applies to simple joint divorce applications, no court appearances, no drafting or finalising any further court documentations, and excludes disbursements costs including court filing fee.</p>
    </section>
  </main>
</body>
</html>
```